Business card design

Hi,
I need to have a business card design based on the current logo.
If competitive I not put it out to everyone.

It can be single of double sided

Target Market(s)

Food businesses

Industry/Entity Type

Food Manufacturing

Contact Information for Business Card

Details will on card will be as follows Name = Marcus Helt Email = Marcus@TalBakery.com.au Phone = 0418562207 Address = 17 Lanford Street , Marlow Heights QLD 4912 Australia

Font styles to use
Other font styles liked:
• based on two fonts - Adelle & Museo

Requirements
Must have
• Based on the on switch concept

```html
<!DOCTYPE html>
<html lang="en">
<head>
<meta charset="utf-8">
<title>TalBakery Business Card</title>
<link href="https://fonts.googleapis.com/css2?family=Varela+Round&family=Zilla+Slab:wght@600&display=swap" rel="stylesheet">
<style>
  :root {
    --brand-red: #e8294a;
    --card-white: #f7f7f7;
    --ink: #2a2a2a;
    --backdrop: #dcdde0;
  }
  * { box-sizing: border-box; margin: 0; padding: 0; }
  html, body {
    width: 1200px; height: 857px; overflow: hidden;
    background: var(--backdrop);
  }
  .canvas {
    width: 1200px; height: 857px;
    display: flex; align-items: center; justify-content: center; gap: 40px;
  }
  .card {
    width: 530px; height: 303px; position: relative;
    box-shadow: 0 2px 10px rgba(0,0,0,.12);
  }
  .card-front { background: var(--card-white); }
  .card-back {
    background: var(--brand-red);
    display: flex; align-items: center; justify-content: center;
  }

  .brand-small {
    position: absolute; left: 38px; top: 40px;
    display: flex; align-items: center; gap: 8px;
    font-family: "Varela Round", sans-serif; font-weight: 400;
    color: var(--brand-red); font-size: 22px; letter-spacing: 1px;
  }
  .brand-dot {
    width: 16px; height: 16px; border-radius: 50%;
    background: var(--brand-red);
  }

  .contact {
    position: absolute; left: 228px; top: 82px;
    font-family: "Varela Round", sans-serif;
  }
  .contact-name {
    color: var(--brand-red); font-size: 24px; font-weight: 400; letter-spacing: .5px;
  }
  .name-rule {
    width: 52px; height: 2px; background: var(--brand-red);
    margin: 10px 0 22px 4px;
  }
  .contact-list { list-style: none; color: var(--ink); font-size: 13.5px; line-height: 19px; }
  .contact-list li { display: flex; align-items: flex-start; gap: 7px; }
  .contact-list svg { flex: none; width: 13px; height: 13px; margin-top: 3px; fill: var(--brand-red); }

  .brand-lockup { text-align: right; color: #fff; }
  .brand-large {
    display: flex; align-items: center; gap: 14px;
    font-family: "Varela Round", sans-serif; font-weight: 400;
    font-size: 54px; letter-spacing: 3px; line-height: 1;
  }
  .brand-large .brand-dot { width: 34px; height: 34px; background: #fff; }
  .tagline {
    font-family: "Zilla Slab", serif; font-weight: 600;
    font-size: 17px; margin-top: 6px; letter-spacing: .3px;
  }
</style>
</head>
<body>
<main class="canvas">
  <section class="card card-front" aria-label="Business card front">
    <div class="brand-small"><span class="brand-dot"></span>TALBAKERY</div>
    <div class="contact">
      <h1 class="contact-name">Marcus Helt</h1>
      <div class="name-rule"></div>
      <ul class="contact-list">
        <li>
          <svg viewBox="0 0 24 24" aria-hidden="true"><path d="M6.6 10.8a15 15 0 0 0 6.6 6.6l2.2-2.2a1 1 0 0 1 1-.25 11.4 11.4 0 0 0 3.6.57 1 1 0 0 1 1 1V20a1 1 0 0 1-1 1A17 17 0 0 1 3 4a1 1 0 0 1 1-1h3.5a1 1 0 0 1 1 1c0 1.25.2 2.45.57 3.57a1 1 0 0 1-.25 1z"/></svg>
          <span>04 18 56 22 07</span>
        </li>
        <li>
          <svg viewBox="0 0 24 24" aria-hidden="true"><path d="M2 5h20v14H2z"/><path d="M2 5l10 8 10-8" fill="none" stroke="#fff" stroke-width="1.6"/></svg>
          <span>Marcus@TalBakery.com.au</span>
        </li>
        <li>
          <svg viewBox="0 0 24 24" aria-hidden="true"><path d="M12 2a7 7 0 0 0-7 7c0 5.2 7 13 7 13s7-7.8 7-13a7 7 0 0 0-7-7zm0 9.5A2.5 2.5 0 1 1 12 6.5a2.5 2.5 0 0 1 0 5z"/></svg>
          <span>17 Lanford Street , Marlow Heights<br>QLD 4912 Australia</span>
        </li>
      </ul>
    </div>
  </section>

  <section class="card card-back" aria-label="Business card back">
    <div class="brand-lockup">
      <div class="brand-large"><span class="brand-dot"></span>TALBAKERY</div>
      <p class="tagline">Fresh Baking On Request</p>
    </div>
  </section>
</main>
</body>
</html>
```